Vantage Automotive Reconditioning Business Card

We need a professional business card that features our logo, a picture of the employee, and a brief list of our services.
I've attached a logo, and will attach photos at a later date.
The four services that need to be listed are Bumper repair and repainting, road rash repair, clear coat scratch repair, and automotive touch-up.
Target Market(s)
30 - 40 year male general managers of automobile dealerships. They are used to seeing every vendor gimmick under the sun. This brochure needs to impress with its simplicity and honesty.
Industry/Entity Type
Automotive
Look and feel
Each slider illustrates characteristics of the customer's brand and the style your logo design should communicate.

```html
<!DOCTYPE html>
<html lang="en">
<head>
<meta charset="utf-8">
<title>Vantage Automotive Reconditioning – Business Card</title>
<link rel="stylesheet" href="https://fonts.googleapis.com/css2?family=Open+Sans:wght@400;600;800&display=swap">
<style>
  :root {
    --page-bg: #d9d8d5;
    --card-white: #f7f7f6;
    --card-dark: #2b2b2b;
    --ink: #2a2a2a;
    --ink-soft: #3c3c3c;
    --accent: #e8461b;
    --suit-light: #4c6ea6;
    --suit-dark: #1f3460;
  }
  * { box-sizing: border-box; margin: 0; padding: 0; }
  html, body { width: 1200px; height: 900px; overflow: hidden; }
  body {
    background: var(--page-bg);
    font-family: "Open Sans", Arial, sans-serif;
    position: relative;
  }
  .card {
    position: absolute;
    left: 250px;
    width: 700px;
    height: 400px;
    border-radius: 22px;
    overflow: hidden;
    box-shadow: 0 6px 18px rgba(0,0,0,.18);
  }

  /* ---------- Back ---------- */
  .card--back { top: 35px; background: var(--card-dark); }
  .card--back .brand {
    position: absolute; top: 95px; left: 0; right: 0;
    text-align: center; color: #ffffff;
  }
  .brand__name {
    font-weight: 800; font-size: 64px; line-height: 1;
    letter-spacing: 2px; text-transform: uppercase;
  }
  .brand__tag {
    font-weight: 800; font-size: 15px; letter-spacing: 1.5px;
    text-transform: uppercase; margin-top: 6px;
  }
  .services-strip {
    position: absolute; left: 0; right: 0; top: 292px; height: 38px;
    background: var(--card-white);
    border-top: 3px solid var(--accent);
    border-bottom: 3px solid var(--accent);
    color: var(--ink); font-size: 13px; font-weight: 400;
    display: flex; align-items: center; justify-content: center;
  }

  /* ---------- Front ---------- */
  .card--front { top: 465px; background: var(--card-white); }
  .card--front .brand {
    position: absolute; top: 48px; left: 330px; color: var(--ink);
  }
  .card--front .brand__name { font-size: 60px; }
  .card--front .brand__tag { font-size: 14px; margin-top: 4px; }

  .portrait {
    position: absolute; left: 110px; top: 140px;
    width: 240px; height: 190px;
    background: linear-gradient(160deg, var(--suit-light), var(--suit-dark));
    border-radius: 90px 90px 0 0;
  }

  .contact {
    position: absolute; left: 380px; top: 172px;
    color: var(--ink-soft); font-size: 14px; line-height: 18px;
  }
  .contact__address { margin-bottom: 8px; }
  .contact__row { display: flex; align-items: center; gap: 10px; height: 22px; }
  .contact__row svg { width: 14px; height: 14px; fill: var(--accent); flex: none; }

  .name-band {
    position: absolute; left: 0; top: 330px; width: 660px; height: 48px;
    background: var(--card-dark);
    border-top: 3px solid var(--accent);
    display: flex; align-items: center; padding-left: 40px;
  }
  .name-band__name {
    color: #ffffff; font-size: 24px; font-weight: 600;
    letter-spacing: 3px; text-transform: uppercase;
  }
  .band-tip { position: absolute; left: 660px; top: 330px; width: 40px; height: 48px; }
</style>
</head>
<body>

  <section class="card card--back" aria-label="Card back">
    <div class="brand">
      <div class="brand__name">Vantage</div>
      <div class="brand__tag">Automotive Reconditioning</div>
    </div>
    <div class="services-strip">
      Bumper repair and repainting &nbsp;|&nbsp; Road rash repair &nbsp;|&nbsp; Clear coat scratch repair &nbsp;|&nbsp; Automotive touch-up
    </div>
  </section>

  <section class="card card--front" aria-label="Card front">
    <div class="brand">
      <div class="brand__name">Vantage</div>
      <div class="brand__tag">Automotive Reconditioning</div>
    </div>

    <div class="portrait" role="img" aria-label="Employee photo: man in a blue pinstripe suit with arms folded"></div>

    <div class="contact">
      <div class="contact__address">4820 E. Cactus Ridge Rd.<br>Mesa, AZ 85201</div>
      <div class="contact__row">
        <svg viewBox="0 0 16 16" aria-hidden="true"><path d="M3 1h3l1.5 4-2 1.3a9 9 0 0 0 4.2 4.2L11 8.5l4 1.5v3a2 2 0 0 1-2 2A12 12 0 0 1 1 3a2 2 0 0 1 2-2z"/></svg>
        <span>555-201-4470</span>
      </div>
      <div class="contact__row">
        <svg viewBox="0 0 16 16" aria-hidden="true"><path d="M4.5 0h7A1.5 1.5 0 0 1 13 1.5v13a1.5 1.5 0 0 1-1.5 1.5h-7A1.5 1.5 0 0 1 3 14.5v-13A1.5 1.5 0 0 1 4.5 0zM5 2v10h6V2zm3 11a1 1 0 1 0 0 2 1 1 0 0 0 0-2z"/></svg>
        <span>555-201-4480</span>
      </div>
      <div class="contact__row">
        <svg viewBox="0 0 16 16" aria-hidden="true"><path d="M0 3h16v10H0zm1.5 1.5v.3L8 9l6.5-4.2v-.3zm0 2.1v4.9h13V6.6L8 10.8z"/></svg>
        <span>info@vantageauto.com</span>
      </div>
      <div class="contact__row">
        <svg viewBox="0 0 16 16" aria-hidden="true"><path d="M8 0a8 8 0 1 0 0 16A8 8 0 0 0 8 0zm5.9 7.2h-2.7a12 12 0 0 0-1-5A6.5 6.5 0 0 1 13.9 7.2zM8 1.6c.9 1.2 1.5 3.2 1.6 5.6H6.4C6.5 4.8 7.1 2.8 8 1.6zM5.8 2.2a12 12 0 0 0-1 5H2.1a6.5 6.5 0 0 1 3.7-5zM2.1 8.8h2.7a12 12 0 0 0 1 5 6.5 6.5 0 0 1-3.7-5zM8 14.4c-.9-1.2-1.5-3.2-1.6-5.6h3.2c-.1 2.4-.7 4.4-1.6 5.6zm2.2-.6a12 12 0 0 0 1-5h2.7a6.5 6.5 0 0 1-3.7 5z"/></svg>
        <span>www.vantageauto.com</span>
      </div>
    </div>

    <div class="name-band"><span class="name-band__name">Daniel Reyes</span></div>
    <svg class="band-tip" viewBox="0 0 40 48" aria-hidden="true">
      <polygon points="0,0 22,0 0,48" fill="var(--card-dark)"/>
      <polygon points="0,0 24,0 24,3 0,3" fill="var(--accent)"/>
      <polygon points="22,0 34,0 30,10" fill="var(--accent)"/>
    </svg>
  </section>

</body>
</html>
```